Marco Bellin Photography needs a business card designs

I am looking for a business card with a logo clean and simple which I can use that logo on my website or on my pictures. It has to be very classy and very professional. Please look at my website at www.marcobphoto.com for my signature. I'm thinking of something like that for my signature/logo. I'm still working on my website but you get an idea. I'm open to any design but not too busy graphics.

I will be printing the business card from kelvaprint.com.

Surprise me :)

contact me if you have any questions.

-MB
Updates

I'm receiving a lot of black background at the moment. I know my website is all black doesn't mean I want my card to be all black. Please send in with some white background as well. Thanks :)

check out some business cards that I found online. I think they are simple and look really awesome. I don't want a card that is too busy.

http://www.marcobphoto.com/p270092084

Reason: Please extend the date for me. I haven't really receive any good design yet.

Industry/Entity Type

Printing

Requirements
Nice to have
• -a logo that related to my first and last initial of my name "MB"
-double sided
Should not have
• -I don't want my background to be all black.
-no pictures on the card

```html
<!DOCTYPE html>
<html lang="en">
<head>
<meta charset="utf-8">
<title>Marco Bellin Photography – Business Card</title>
<link rel="stylesheet" href="https://fonts.googleapis.com/css2?family=Lato:wght@400&display=swap">
<style>
  :root {
    --page-bg: #ffffff;
    --card-bg: #ffffff;
    --card-edge: #222222;
    --name-tint: #e3e3e3;
    --ink: #1a1a1a;
  }
  * { margin: 0; padding: 0; box-sizing: border-box; }
  html, body {
    width: 1200px;
    height: 900px;
    overflow: hidden;
    background: var(--page-bg);
  }
  .canvas {
    position: relative;
    width: 1200px;
    height: 900px;
  }
  .card {
    position: absolute;
    left: 340px;
    top: 16px;
    width: 520px;
    height: 866px;
    background: var(--card-bg);
    border: 2px solid var(--card-edge);
    overflow: hidden;
  }
  .brand-name {
    position: absolute;
    left: 58px;
    top: 120px;
    font-family: "Lato", sans-serif;
    font-weight: 400;
    font-size: 56px;
    line-height: 68px;
    color: var(--name-tint);
  }
  .contact {
    position: absolute;
    left: 52px;
    top: 380px;
    display: flex;
    font-family: "Lato", sans-serif;
    font-weight: 400;
    font-size: 26px;
    line-height: 41px;
    color: var(--ink);
  }
  .contact-labels {
    list-style: none;
    width: 30px;
    text-align: center;
    margin-right: 12px;
  }
  .contact-rule {
    width: 3px;
    background: var(--ink);
    margin: 6px 12px 4px 0;
  }
  .contact-values { list-style: none; }
</style>
</head>
<body>
<main class="canvas">
  <section class="card" aria-label="Marco Bellin Photography business card">
    <p class="brand-name" aria-hidden="true">Marco Bellin<br>Photography</p>
    <div class="contact">
      <ul class="contact-labels" aria-hidden="true">
        <li>p</li>
        <li>e</li>
        <li>w</li>
      </ul>
      <div class="contact-rule"></div>
      <ul class="contact-values">
        <li class="contact-phone">9361 2047</li>
        <li class="contact-email">marcobphoto@postvia.com</li>
        <li class="contact-web">www.marcobphoto.com</li>
      </ul>
    </div>
  </section>
</main>
</body>
</html>
```